Design business cards for Ironvale Barbers (Opening March so won't need finalised till January2018

Ironvale Barbers is the new age barbers and skincare for all men. Creating tailor made haircuts & customised skincare solutions for the perfect healthy manly look. The Barbers will have a industrial, rustic, worldly feel about it. Rustic red brick wall with old wine barrels as the work stations with the old fashion barber chairs. Concrete floor and a bit corrugated iron around.
Target Market(s)
Professional males who like a great haircut, wet shave and may consider a facial if in the right environment. Total pampering experience in a boys environment.
Industry/Entity Type
Barber
Contact Information for Business Card
Front- Logo - address is 42 Kowhai Rd Taupo
Ph - (07) 348 6192
www.ironvalebarbers.com
email - hello@ironvale.co.nz
Back of card
Mens Haircare - Wet Shaving - Facials - Skin Prescriptions
We are doing a loyalty program - 6 squares numbered then 7th free
Colors
Designer to choose colors to be used in the design.
Requirements
Must have
- Clean simple easy to read.
Nice to have
- Our current colours are white font on black background but thinking we need to introduce another colour. Maybe white logo on a copper, bronze or rusty background. Or even a rustic red brick wall with white writing. Want it clean simple to read. Maybe a burgundy?
Should not have
- no images like heads, scissors, razors please

```html
<!DOCTYPE html>
<html lang="en">
<head>
<meta charset="utf-8">
<title>Ironvale Barbers – Business Cards</title>
<link href="https://fonts.googleapis.com/css2?family=Roboto+Condensed:wght@700&display=swap" rel="stylesheet">
<style>
  :root {
    --page: #ffffff;
    --burgundy: #3e0003;
    --rust: #6f2d24;
    --guide: #5c1c1c;
    --white: #ffffff;
  }
  * { box-sizing: border-box; margin: 0; padding: 0; }
  html, body { width: 1200px; height: 1200px; overflow: hidden; background: var(--page); }
  body { position: relative; font-family: "Roboto Condensed", "Arial Narrow", sans-serif; font-weight: 700; }

  .card {
    position: absolute;
    width: 736px;
    height: 409px;
    background: var(--burgundy);
    overflow: hidden;
  }
  .card--front { left: 232px; top: 133px; }
  .card--back  { left: 234px; top: 613px; }

  .frame {
    position: absolute;
    left: 41px; top: 41px;
    width: 656px; height: 327px;
    border: 1px solid var(--guide);
  }
  .frame::after {
    content: "";
    position: absolute;
    inset: 6px;
    border: 1px solid var(--guide);
  }
  .grid { position: absolute; left: 41px; top: 41px; width: 656px; height: 327px; }

  .region-map {
    position: absolute;
    left: 256px; top: 55px;
    width: 240px; height: 302px;
    background: radial-gradient(ellipse at 55% 50%, rgba(111,45,36,0.75) 0%, rgba(111,45,36,0.35) 55%, rgba(111,45,36,0) 75%);
  }

  .wordmark {
    position: absolute;
    left: 0; right: 0; top: 172px;
    text-align: center;
    color: var(--white);
    font-size: 46px;
    line-height: 1;
    letter-spacing: 1px;
    text-transform: uppercase;
  }

  .contact {
    position: absolute;
    top: 302px;
    color: var(--white);
    font-size: 19px;
    line-height: 23px;
    letter-spacing: 0.6px;
  }
  .contact--left { left: 58px; }
  .contact--right { right: 58px; text-align: right; }

  .services {
    position: absolute;
    left: 239px; top: 80px;
    list-style: none;
    color: var(--rust);
    font-size: 29px;
    line-height: 34.5px;
    letter-spacing: 0.8px;
  }

  .booking-field {
    position: absolute;
    left: 238px;
    width: 258px;
    color: var(--white);
    font-size: 22px;
    line-height: 1;
    padding-bottom: 6px;
    border-bottom: 1px solid var(--white);
    letter-spacing: 0.4px;
  }
  .booking-field--date { top: 250px; }
  .booking-field--time { top: 302px; }
</style>
</head>
<body>

  <section class="card card--front" aria-label="Front of card">
    <div class="frame"></div>
    <svg class="grid" width="656" height="327" viewBox="0 0 656 327" aria-hidden="true">
      <g stroke="#5c1c1c" stroke-width="1">
        <line x1="160" y1="0" x2="160" y2="327"/>
        <line x1="368" y1="0" x2="368" y2="327"/>
        <line x1="576" y1="0" x2="576" y2="327"/>
        <line x1="0" y1="109" x2="656" y2="109"/>
        <line x1="0" y1="217" x2="656" y2="217"/>
      </g>
    </svg>
    <div class="region-map" role="img" aria-label="Silhouette map of New Zealand and Tasmania in rust tone"></div>

    <h1 class="wordmark">Ironvale Barbers</h1>

    <p class="contact contact--left">42 Kowhai Rd Taupo<br>+64 27 514 3870</p>
    <p class="contact contact--right">hello@ironvale.co.nz<br>www.ironvalebarbers.com</p>
  </section>

  <section class="card card--back" aria-label="Back of card">
    <div class="frame"></div>
    <ul class="services">
      <li>Mans Haircare</li>
      <li>Wet Shaving</li>
      <li>Facials</li>
      <li>Skin Prescriptions</li>
    </ul>
    <p class="booking-field booking-field--date">Date</p>
    <p class="booking-field booking-field--time">Time</p>
  </section>

</body>
</html>
```